Einladungskarten für Benefizveranstaltung
Zielgruppe
vorrangig Unternehmer;
Privatpersonen
Sportbegeisterte
Aufgabenstellung
Wir benötigen für eine Veranstaltung mit 3 Terminen an 3 vers. Standorten zwei Einladungskarten.
1.) off. Einladung & 2.) VIP-Einladung
Bei der Veranstaltung handelt es sich um einen Vortrag des blinden Bergsteigers Timo Brandler, der alle Seven Summits (die höchsten Gifpel der Kontinente) erreichen möchte. www.timobrandler-vortrag.com
Die Betriebs-Forum unterstützt ihn dabei und braucht die Hilfe von anderen Unternehmen & Privatpersonen. Diese werden zur Veranstaltung eingeladen.
Das Design der Einladungskarten soll an unser Corporate Design angepasst werden (www.betriebs-forum.eu) aber auch den Aspekt "Bergsteigen, Natur, Timo Brandler" beinhalten.

```html
<!DOCTYPE html>
<html lang="de">
<head>
<meta charset="utf-8">
<title>Betriebs-Forum 2011 – Balanceakt</title>
<link rel="stylesheet" href="https://fonts.googleapis.com/css2?family=Source+Sans+3:ital,wght@0,300;0,400;0,600;0,700;1,400&display=swap">
<style>
  :root {
    --orange: #e5601e;
    --text: #555a60;
    --text-light: #8b9096;
    --rule: #c9ccd0;
    --paper: #ffffff;
    --stage: #ebebeb;
    --sky-deep: #2c5ca5;
    --sky-mid: #7ea6d4;
    --snow: #e9eff6;
    --snow-shade: #c9d6e5;
    --partner-blue: #2f7cc0;
    --partner-red: #7d2a31;
    --form-band: #f3f3f3;
    --font: "Source Sans 3", "Myriad Pro", Arial, sans-serif;
  }
  * { box-sizing: border-box; margin: 0; padding: 0; }
  html, body { width: 1200px; height: 1200px; overflow: hidden; }
  body { background: var(--stage); font-family: var(--font); color: var(--text); }
  .canvas { position: relative; width: 1200px; height: 1200px; overflow: hidden; }

  .sheet { position: absolute; background: var(--paper); box-shadow: 0 2px 6px rgba(0,0,0,.12); overflow: hidden; }
  .abs { position: absolute; }

  /* brand name stand-in: plain text only */
  .brand { position: absolute; color: var(--orange); font-weight: 600; white-space: nowrap; line-height: 1; }

  /* ---------- Cover ---------- */
  .cover { left: 40px; top: 210px; width: 540px; height: 780px; }
  .cover-peaks { left: 6px; top: 40px; width: 380px; height: 150px;
    background: linear-gradient(180deg, rgba(236,238,240,0) 0%, #f0f1f3 60%, #f7f8f9 100%); }
  .cover .brand { right: 30px; top: 88px; font-size: 26px; }
  .cover-title { left: 36px; top: 188px; font-size: 27px; font-weight: 400; color: var(--orange); letter-spacing: .2px; }
  .cover-dates { left: 0; top: 223px; width: 100%; padding-left: 36px; display: flex; font-size: 14px; color: var(--text-light); letter-spacing: .6px; border-top: 1px solid #e3e4e6; padding-top: 2px; }
  .cover-dates span { padding: 0 9px; border-left: 1px solid var(--rule); }
  .cover-dates span:first-child { padding-left: 0; border-left: 0; }
  .cover-photo { left: 0; top: 246px; width: 540px; height: 534px;
    background: linear-gradient(180deg, var(--sky-deep) 0%, #4a78bb 14%, var(--sky-mid) 30%, #b6c9e0 40%, #9fb3cc 44%, #dfe7f1 52%, var(--snow) 62%, var(--snow-shade) 80%, #dce5ef 100%); }
  .cover-headline { left: 34px; top: 258px; font-size: 44px; font-weight: 700; color: #fff; letter-spacing: 1px; line-height: 1; }
  .cover-headline span { color: var(--orange); }
  .cover-sub { left: 34px; top: 308px; font-size: 22px; font-weight: 300; color: #fff; letter-spacing: .3px; }
  .summit { position: absolute; display: flex; align-items: center; gap: 5px; font-size: 11.5px; font-style: italic; color: #4d5b6e; }
  .summit::before { content: ""; width: 5px; height: 5px; border-radius: 50%; background: var(--orange); }

  /* ---------- Inside spread ---------- */
  .spread { left: 610px; top: 82px; width: 550px; height: 390px; }
  .spread-photo { top: 0; height: 88px; }
  .spread-photo--portrait { left: 0; width: 149px; background: linear-gradient(160deg, #3b6fb2 0%, #c7d4e2 45%, #b83a3a 80%, #6a2a2a 100%); }
  .spread-photo--rock { left: 149px; width: 142px; background: linear-gradient(180deg, #6d94c6 0%, #9b9a96 45%, #7c7b77 100%); }
  .spread-photo--summit { left: 291px; width: 138px; border-bottom-right-radius: 14px; background: linear-gradient(180deg, #1f56a6 0%, #5f8fcc 50%, #e9eef5 80%, #cdd8e6 100%); }
  .spread-strip { left: 0; top: 88px; width: 443px; height: 4px; background: #d8dadd; border-bottom-right-radius: 4px; }
  .spread .brand { left: 452px; top: 40px; font-size: 11.5px; }
  .page-right-bg { left: 268px; top: 92px; width: 282px; height: 298px; background: linear-gradient(90deg, #e8e8e8 0%, #f8f8f8 18%, #fff 45%); }
  .page-left { left: 20px; top: 128px; width: 215px; font-size: 7.4px; line-height: 1.6; }
  .page-left p + p { margin-top: 6px; }
  .page-left em { font-style: normal; color: var(--orange); }
  .page-right { left: 312px; top: 118px; width: 215px; font-size: 7.4px; line-height: 1.55; }
  .page-right h3 { font-size: 13px; font-weight: 400; color: var(--orange); line-height: 1.2; }
  .page-right h4 { font-size: 7.8px; font-weight: 600; color: var(--orange); margin-top: 7px; }
  .page-right dl { display: grid; grid-template-columns: 44px 1fr; padding-left: 10px; margin: 1px 0 8px; }
  .page-right dd { margin: 0; }
  .page-right .indent { padding-left: 10px; }
  .page-right strong { font-weight: 700; }
  .partner-shape { position: absolute; background: #c4c6ca; }
  .partner-shape--oval { left: 165px; top: 364px; width: 16px; height: 11px; border-radius: 50%; background: #8e939a; }
  .partner-shape--bar { left: 186px; top: 366px; width: 26px; height: 7px; }
  .partner-shape--line { left: 310px; top: 366px; width: 42px; height: 5px; background: #d6d7d9; }
  .partner-shape--block { left: 370px; top: 361px; width: 20px; height: 14px; background: var(--partner-red); }
  .partner-advisor { left: 420px; top: 361px; display: flex; align-items: center; gap: 5px; }
  .partner-advisor i { width: 14px; height: 14px; background: var(--partner-blue); }
  .partner-advisor span { font-size: 7.4px; font-weight: 600; color: var(--partner-blue); line-height: 1.15; width: 100px; }

  /* ---------- Reply form ---------- */
  .reply { left: 670px; top: 512px; width: 430px; height: 616px; }
  .reply-title { left: 34px; top: 44px; font-size: 18px; font-weight: 400; color: var(--text); }
  .reply-title span { color: var(--orange); }
  .reply-lead { left: 34px; top: 128px; font-size: 10px; color: var(--orange); }
  .reply-options { left: 34px; top: 152px; display: flex; gap: 18px; font-size: 9.5px; letter-spacing: .3px; }
  .reply-companion { left: 34px; top: 174px; font-size: 9.5px; }
  .reply-band { left: 0; top: 217px; width: 430px; height: 340px; background: linear-gradient(180deg, var(--form-band) 0%, #fff 100%); }
  .reply-photo { left: 400px; top: 212px; width: 30px; height: 404px; border-top-left-radius: 10px;
    background: linear-gradient(180deg, var(--sky-deep) 0%, var(--sky-mid) 30%, var(--snow) 60%, var(--snow-shade) 100%); }
  .field-row { position: absolute; left: 30px; width: 350px; height: 28px; border-bottom: 1px solid var(--rule); }
  .field-row label { position: absolute; top: 2px; font-size: 7.5px; color: var(--orange); }
  .reply-note { left: 34px; top: 500px; width: 340px; font-size: 7.4px; line-height: 1.55; }
  .reply-note em { font-style: normal; color: var(--orange); }
  .reply-host { left: 34px; top: 566px; font-size: 7.4px; line-height: 1.5; }
  .reply-host b { display: block; font-weight: 400; color: var(--orange); }
  .reply .brand { left: 300px; top: 572px; font-size: 11px; }
</style>
</head>
<body>
<main class="canvas">

  <!-- Cover -->
  <section class="sheet cover" aria-label="Einladung Titelseite">
    <div class="abs cover-peaks" role="img" aria-label="Linienzeichnung einer Bergkette in hellem Grau"></div>
    <p class="brand">Betriebs-Forum</p>
    <h1 class="abs cover-title">Betriebs-Forum 2011</h1>
    <p class="abs cover-dates"><span>20. Juni GRAZ</span><span>21. Juni WIEN</span><span>30. Juni INNSBRUCK</span></p>
    <div class="abs cover-photo" role="img" aria-label="Foto einer Gletscherlandschaft unter blauem Himmel, darüber eine helle Weltkarte mit den Seven Summits"></div>
    <h2 class="abs cover-headline">BALANCE<span>AKT</span></h2>
    <p class="abs cover-sub">TIMO BRANDLER – blind climer</p>
    <span class="summit" style="left:76px;top:538px">Denali</span>
    <span class="summit" style="left:312px;top:554px">Mt Elbrus</span>
    <span class="summit" style="left:376px;top:583px">Mt Everest</span>
    <span class="summit" style="left:307px;top:623px">Kilimanjaro</span>
    <span class="summit" style="left:434px;top:654px">Carstensz Pyramid</span>
    <span class="summit" style="left:108px;top:676px">Aconcagua</span>
    <span class="summit" style="left:176px;top:747px">Mt Vinson</span>
  </section>

  <!-- Inside spread -->
  <section class="sheet spread" aria-label="Einladung Innenseiten">
    <div class="abs spread-photo spread-photo--portrait" role="img" aria-label="Foto: Bergsteiger mit Schneebrille und roter Jacke im Schnee"></div>
    <div class="abs spread-photo spread-photo--rock" role="img" aria-label="Foto: Kletterer an einem Felsturm"></div>
    <div class="abs spread-photo spread-photo--summit" role="img" aria-label="Foto: Seilschaft auf einem verschneiten Gipfel"></div>
    <div class="abs spread-strip"></div>
    <p class="brand">Betriebs-Forum</p>
    <div class="abs page-right-bg"></div>

    <div class="abs page-left">
      <p><em>Der Osttiroler Timo Brandler,</em> 44, ist von Geburt an blind. Seit seinem neunten Lebensjahr geht er seiner großen Leidenschaft, dem Klettern, nach und bewältigt auf diese Weise Touren im höchsten Schwierigkeitsgrad. Herzensprojekt ist es, als erster blinder Europäer die 7-Summits – die sieben höchsten Gipfel der Kontinente - zu erreichen. Schon sechs dieser legendären Bergriesen durfte er mit Händen und Füßen berühren.</p>
      <p>Im Frühjahr 2012 will er die Reise zum letzten Gipfel antreten. Zur Verwirklichung dieses Ziels braucht er verlässliche Partner. Denn große Ziele und Erfolge sind ohne eine starke Seilschaft kaum möglich. Timo Brandler weiß, dass Teamgeist in ungeahnte Höhen führt.</p>
      <p><em>Als Mensch,</em> die Mut, Willensstärke und Ausdauer verkörpert, ist Timo Brandler ein Vorbild für die heimischen Wirtschaft. Er zeigt, wie man auch schwierigen Vorhaben unerschrocken begegnet und jede Herausforderung frei angeht.</p>
    </div>

    <div class="abs page-right">
      <h3>Termine</h3>
      <dl>
        <dt>20.06.2011</dt><dd>Veranstaltungszentrum Graz</dd>
        <dt>21.06.2011</dt><dd>Veranstaltungszentrum Wien</dd>
        <dt>30.06.2011</dt><dd>Veranstaltungszentrum Innsbruck</dd>
      </dl>
      <h3>Programm</h3>
      <dl>
        <dt>16:00Uhr</dt><dd>Begrüßung</dd>
        <dt>16:15Uhr</dt><dd>Timo Brandler – „Blind auf die Gipfel der Welt“</dd>
        <dt>18:15Uhr</dt><dd>Get Together am Buffet</dd>
      </dl>
      <h4>Teilnahmegebühr</h4>
      <p class="indent">€ 35.- pro Teilnehmer Anmeldungen werden in der Reihenfolge des Eintreffens und nach Maßgabe freier Plätze berücksichtigt. Wir ersuchen Sie, nach Erhalt der Rechnung die Teilnahmegebühr umgehend zu überweisen.</p>
      <h4>Ermäßigung</h4>
      <p class="indent">Bei Anmeldung &amp; Bezahlung über <strong>www.betriebs-forum.at</strong> verringert sich die Teilnahmegebühr auf € 30.-</p>
    </div>

    <span class="partner-shape partner-shape--oval"></span>
    <span class="partner-shape partner-shape--bar"></span>
    <span class="partner-shape partner-shape--line"></span>
    <span class="partner-shape partner-shape--block"></span>
    <div class="abs partner-advisor"><i></i><span>Ing. Weber Markus Wirtschaftsberatung</span></div>
  </section>

  <!-- Reply form -->
  <section class="sheet reply" aria-label="Anmeldeformular">
    <h2 class="abs reply-title"><span>Anmeldefax</span> +43 512 470213 16</h2>
    <p class="abs reply-lead">Ich nehme an folgender Veranstaltung teil:</p>
    <p class="abs reply-options"><span>O 20.06. GRAZ</span><span>O 21.06. WIEN</span><span>O 30.06. INNSBRUCK</span></p>
    <p class="abs reply-companion">O Ich werde in Begleitung kommen</p>
    <div class="abs reply-band"></div>
    <div class="abs reply-photo" role="img" aria-label="Foto: verschneiter Berghang unter blauem Himmel"></div>

    <div class="field-row" style="top:236px"><label style="left:4px">Titel</label><label style="left:82px">Nachname</label><label style="left:212px">Vorname</label></div>
    <div class="field-row" style="top:271px"><label style="left:4px">Straße/Nr.</label><label style="left:212px">PLZ/Ort</label></div>
    <div class="field-row" style="top:306px"><label style="left:4px">Unternehmen</label></div>
    <div class="field-row" style="top:341px"><label style="left:4px">E-Mail</label></div>
    <div class="field-row" style="top:379px"><label style="left:4px">Telefon</label><label style="left:212px">Fax</label></div>
    <div class="field-row" style="top:439px"><label style="left:4px">Datum</label><label style="left:112px">Unterschrift</label></div>

    <p class="abs reply-note">Aufgrund der begrenzten Teilnehmerzahl bitten wir um Ihre verbindliche Anmeldung bis <em>Freitag, 17. Juni 2011</em>:<br>Tel: +43 512 470213 | Fax: +43 512 470213 16<br>E-Mail: anmeldung@betriebs-forum.at | Web: www.betriebs-forum.at</p>
    <p class="abs reply-host"><b>Veranstalter</b>Betriebs-Forum GmbH | Talstraße 12 | 6020 Innsbruck</p>
    <p class="brand">Betriebs-Forum</p>
  </section>

</main>
</body>
</html>
```